Wine Label Design

We’re a wine company looking to design a new label: “Wayfarer”. The label should promote quality. I would like the label to show a compass and continents. I would like the Continents to cover the whole label and be noticable for the consumers to see. Please review the attached picture it will give you a good example of the continents design.. Also, place the compass on the top capsule and make the capsule the same dominate color as your label.

Front label dimensions: 4 H x 4 W
-Brand Name: Wayfarer
-Wine Type: Zinfandel
-Vintage: 2012
-Region: Sonoma County

Back label dimensions: 3.5 H x 3.5 W
- brand name: Wayfarers
- Vintage: 2012
- Region: Sonoma County
-Alcohol statement: Alc. 14.0% by vol. (exactly 2 mm in height)
-Volume: 750 ml (exactly 2 mm in height)

WWW.HOLBROOKWINECO.EXAMPLE (exactly 2 mm in height)

GOVERNMENT WARNING: (1) ACCORDING TO THE SURGEON GENERAL, WOMEN SHOLD NOT DRINK ALCOHOLIC BEVERAGES DURING PREGNANY BECAUSE OF THE RISK OF BIRTH DEFECTS. (2) CONSUMPTION OF ALCOHOLIC BEVERAGES IMPAIRS YOUR ABILITY TO DRIVE A CAR OR OPERATE MACHINERY, AND MAY CAUSE HEALTH PROBLEMS. (exactly 2 mm in height) (This needs to be blocked/justified format

CONTAINS SULFITES (exactly 2 mm in height)
Updates

thanks for all of your submittals.  I updated the brief for your review.

Target Market(s)

Wayfraers

Industry/Entity Type

Government

Font styles to use
Serif
Sans Serif
Decorative

Requirements
Must have
• Compass and continents

```html
<!DOCTYPE html>
<html lang="en">
<head>
<meta charset="utf-8">
<title>Wayfarer Zinfandel – Back Label</title>
<link rel="stylesheet" href="https://fonts.googleapis.com/css2?family=EB+Garamond:wght@400;500;600;700&family=Oswald:wght@400;500;600&display=swap">
<style>
  :root {
    --page: #ffffff;
    --label-cream: #f0efb2;
    --label-cream-deep: #ecebab;
    --frame-pink: #e57ad6;
    --brand-red: #c8102e;
    --ink-brown: #3d1a08;
  }
  * { margin: 0; padding: 0; box-sizing: border-box; }
  html, body {
    width: 1200px;
    height: 900px;
    overflow: hidden;
    background: var(--page);
  }
  .canvas {
    position: relative;
    width: 1200px;
    height: 900px;
  }
  .back-label {
    position: absolute;
    left: 486px;
    top: 336px;
    width: 227px;
    height: 227px;
    background: var(--label-cream);
  }
  .continents-field {
    position: absolute;
    inset: 0;
    background: linear-gradient(160deg, var(--label-cream) 0%, var(--label-cream-deep) 100%);
  }
  .label-frame {
    position: absolute;
    left: 5px;
    top: 6px;
    width: 217px;
    height: 216px;
    border: 2px solid var(--frame-pink);
  }
  .label-content {
    position: absolute;
    inset: 0;
    color: var(--ink-brown);
    text-align: center;
  }
  .brand-name {
    position: absolute;
    left: 0; right: 0;
    top: 11px;
    font-family: "EB Garamond", serif;
    font-weight: 700;
    font-size: 26px;
    line-height: 26px;
    letter-spacing: 0.3px;
    color: var(--brand-red);
  }
  .varietal {
    position: absolute;
    left: 0; right: 0;
    top: 37px;
    font-family: "EB Garamond", serif;
    font-weight: 600;
    font-size: 13px;
    line-height: 14px;
    letter-spacing: 0.5px;
  }
  .vintage {
    position: absolute;
    left: 0; right: 0;
    top: 51px;
    font-family: "EB Garamond", serif;
    font-weight: 600;
    font-size: 11px;
    line-height: 12px;
    letter-spacing: 1px;
    font-variant-numeric: oldstyle-nums;
  }
  .story {
    position: absolute;
    left: 8px; right: 8px;
    top: 65px;
    font-family: "EB Garamond", serif;
    font-weight: 600;
    font-size: 7px;
    line-height: 9.6px;
  }
  .region {
    position: absolute;
    left: 0; right: 0;
    top: 146px;
    font-family: "EB Garamond", serif;
    font-weight: 500;
    font-size: 11.5px;
    line-height: 12px;
    letter-spacing: 0.9px;
  }
  .government-warning {
    position: absolute;
    left: 15px;
    width: 198px;
    top: 161px;
    font-family: "Oswald", sans-serif;
    font-weight: 400;
    font-size: 6.3px;
    line-height: 9.4px;
  }
  .government-warning .line {
    display: block;
    text-align: justify;
    text-align-last: justify;
    white-space: nowrap;
  }
  .government-warning strong { font-weight: 600; }
  .legal-line {
    position: absolute;
    left: 15px;
    width: 198px;
    top: 203px;
    display: flex;
    justify-content: space-between;
    font-family: "Oswald", sans-serif;
    font-weight: 400;
    font-size: 8.6px;
    line-height: 10px;
    letter-spacing: 0.2px;
  }
</style>
</head>
<body>
<main class="canvas">
  <section class="back-label" aria-label="Wayfarer Zinfandel back label">
    <div class="continents-field" role="img" aria-label="World continents map with a compass across the label"></div>
    <div class="label-frame"></div>
    <div class="label-content">
      <h1 class="brand-name">WAYFARER</h1>
      <p class="varietal">ZINFANDEL</p>
      <p class="vintage">2012</p>
      <p class="story">
        Daniel and I have traveled the world visiting wineries and<br>
        vineyards in Europe, Africa, Australia and North and<br>
        South America, from high and low end to large commercial<br>
        and small back roads settings. Our journey moved us to start a<br>
        label of our own to share the amazing experiences we enjoyed<br>
        with the world. Share your wine travel destination experience<br>
        in a photo with our Wayfarers brand at our website<br>
        www.holbrookwineco.example
      </p>
      <p class="region">SONOMA COUNTY</p>
      <p class="government-warning">
        <span class="line"><strong>GOVERNMENT WARNING:</strong> (1) ACCORDING TO THE SURGEON GENERAL, WOMEN SHOULD</span>
        <span class="line">NOT DRINK ALCOHOLIC BEVERAGES DURING PREGNANCY BECAUSE OF THE RISK OF</span>
        <span class="line">BIRTH DEFECTS. (2) CONSUMPTION OF ALCOHOLIC BEVERAGES IMPAIRS YOUR</span>
        <span class="line">ABILITY TO DRIVE A CAR OR OPERATE MACHINERY, AND MAY CAUSE HEALTH PROBLEMS.</span>
      </p>
      <p class="legal-line">
        <span class="alcohol">ALC 14.0% BY VOL</span>
        <span class="sulfites">CONTAINS SULFITES</span>
        <span class="volume">750ML</span>
      </p>
    </div>
  </section>
</main>
</body>
</html>
```